Save our Business Card - We need your help

We need a fresh look on our business cards. We like it as it is, but it's not quite getting the 'wow' effect that we desire.
We're a tech startup building a cloud based solution for retailers consisting of Point of Sale, Inventory management and CRM.
The design should communicate a sense of a company that cares about the little things, design and relationships.
You can have a look at our website www.tillnest.com to get a feel for what we're like. Please feel free to message us for any further clarification
Target Market(s)
Our Customers are retail busines owners, cafe owners, other startups etc.
Industry/Entity Type
Building
Colors
Designer to choose colors to be used in the design.
Look and feel
Each slider illustrates characteristics of the customer's brand and the style your logo design should communicate.

```html
<!DOCTYPE html>
<html lang="en">
<head>
<meta charset="utf-8">
<title>TillNest Business Card</title>
<link href="https://fonts.googleapis.com/css2?family=Quicksand:wght@500;600&family=Ubuntu:wght@700&display=swap" rel="stylesheet">
<style>
  :root {
    --page: #ffffff;
    --label: #8a8a8a;
    --charcoal: #222325;
    --charcoal-light: #3c3d40;
    --charcoal-dark: #1b1c1e;
    --orange: #e8892a;
    --orange-light: #efa033;
    --orange-dark: #dc7a22;
    --white: #ffffff;
    --ghost: rgba(255, 255, 255, 0.06);
    --ghost-warm: rgba(255, 255, 255, 0.1);
  }
  * { margin: 0; padding: 0; box-sizing: border-box; }
  html, body {
    width: 1102px; height: 1200px; overflow: hidden;
    background: var(--page);
  }
  .canvas { position: relative; width: 1102px; height: 1200px; }
  .side-label {
    position: absolute; left: 64px;
    font: 500 17px "Quicksand", sans-serif; color: var(--label);
  }
  .side-label--front { top: 68px; }
  .side-label--back { top: 596px; }

  .card {
    position: absolute; left: 126px; width: 914px; height: 507px; overflow: hidden;
  }
  /* Front */
  .card--front {
    top: 72px;
    background: radial-gradient(ellipse 420px 300px at 440px 250px, var(--charcoal-light), var(--charcoal) 60%, var(--charcoal-dark));
  }
  .front__band {
    position: absolute; top: 0; left: 800px; width: 53px; height: 100%;
    background: var(--orange);
  }
  .front__strip {
    position: absolute; top: 0; left: 853px; width: 61px; height: 100%;
    background: var(--charcoal);
  }
  .front__web {
    position: absolute; left: 883px; top: 253px;
    transform: translate(-50%, -50%) rotate(-90deg);
    white-space: nowrap;
    font: 500 19px "Quicksand", sans-serif; letter-spacing: 1px; color: var(--white);
  }
  .front__mark {
    position: absolute; left: 0; top: 380px; width: 190px; height: 127px;
    background: var(--ghost);
  }
  .brand {
    position: absolute; left: 258px; top: 224px;
    display: flex; align-items: center; gap: 16px;
  }
  .brand__square { width: 48px; height: 48px; background: var(--orange); }
  .brand__name {
    font: 700 50px "Ubuntu", sans-serif; color: var(--orange); line-height: 1;
  }

  /* Back */
  .card--back {
    top: 600px;
    background: radial-gradient(ellipse 520px 340px at 520px 230px, var(--orange-light), var(--orange) 55%, var(--orange-dark));
  }
  .back__strip {
    position: absolute; left: 61px; top: 0; width: 56px; height: 100%;
    background: var(--charcoal);
  }
  .back__namebox {
    position: absolute; left: 117px; top: 48px; width: 357px; height: 107px;
    background: var(--charcoal);
  }
  .back__mark {
    position: absolute; left: 714px; top: 300px; width: 200px; height: 207px;
    background: var(--ghost-warm);
  }
  .person__name {
    position: absolute; left: 139px; top: 66px;
    font: 500 38px "Quicksand", sans-serif; color: var(--white); white-space: nowrap;
  }
  .person__role {
    position: absolute; left: 140px; top: 112px;
    font: 500 16px "Quicksand", sans-serif; color: var(--white);
  }
  .contact { position: absolute; left: 139px; font: 500 20px/25px "Quicksand", sans-serif; color: var(--white); }
  .contact--phone { top: 264px; }
  .contact--email { top: 306px; }
  .contact--address { top: 349px; }
  .icon { position: absolute; left: 79px; width: 22px; height: 22px; }
  .icon--phone { top: 266px; }
  .icon--email { top: 309px; }
  .icon--pin { top: 350px; }
</style>
</head>
<body>
<main class="canvas">
  <p class="side-label side-label--front">Front</p>
  <section class="card card--front">
    <div class="front__mark" role="img" aria-label="Faint brand decoration"></div>
    <div class="brand">
      <span class="brand__square"></span>
      <span class="brand__name">TillNest</span>
    </div>
    <div class="front__band"></div>
    <div class="front__strip"></div>
    <p class="front__web">www.tillnest.com</p>
  </section>

  <p class="side-label side-label--back">Back</p>
  <section class="card card--back">
    <div class="back__mark" role="img" aria-label="Faint brand decoration"></div>
    <div class="back__strip"></div>
    <div class="back__namebox"></div>
    <h1 class="person__name">Mr. Alan Reyes</h1>
    <p class="person__role">CEO and Co Founder</p>

    <svg class="icon icon--phone" viewBox="0 0 22 22" fill="none" stroke="#fff" stroke-width="1.4">
      <path d="M2 8c0-3 4-4 9-4s9 1 9 4l-1 2-3-1V7H6v2l-3 1z"/>
      <rect x="4" y="11" width="14" height="7" rx="1"/>
      <circle cx="11" cy="14.5" r="2"/>
    </svg>
    <p class="contact contact--phone">+(603) 2741 0938</p>

    <svg class="icon icon--email" viewBox="0 0 22 22" fill="none" stroke="#fff" stroke-width="1.4">
      <rect x="2" y="5" width="18" height="12"/>
      <path d="M2 5l9 7 9-7"/>
    </svg>
    <p class="contact contact--email">support@tillnest.com</p>

    <svg class="icon icon--pin" viewBox="0 0 22 22" fill="none" stroke="#fff" stroke-width="1.4">
      <path d="M11 21s-6-7-6-11a6 6 0 0 1 12 0c0 4-6 11-6 11z"/>
      <circle cx="11" cy="10" r="2.2"/>
    </svg>
    <p class="contact contact--address">Unit B-3-12, Block A7 Parkview<br>Jalan Meranti Jaya 47810<br>Shah Alam Selangor, Malaysia</p>
  </section>
</main>
</body>
</html>
```